Demolition Company Billboard Design 13 feet wide 15 feet high

This is my first billboard on a busy road. I want it to be professional but with some eye catching flair that matches by business which is a demoltion business and also list my services. My company slogan is also

"call hollick, watch it fall"

Target Market(s)

Home Ownerd and General Construction Companies

Industry/Entity Type

construction

Colors
0054AA
0677BA
7BADD7
CADEEF
E8F1F8

Requirements
Must have
• My services listed in the pictures my website and my phone number

```html
<!DOCTYPE html>
<html lang="en">
<head>
<meta charset="UTF-8">
<title>Hollick Demolition Billboard</title>
<link rel="stylesheet" href="https://fonts.googleapis.com/css2?family=Anton&family=Oswald:wght@300;400;600&display=swap">
<style>
  :root {
    --page-bg: #e8edf2;
    --white: #ffffff;
    --yellow: #fdc925;
    --blue-top: #2a7399;
    --blue-mid: #2f5a93;
    --blue-bottom: #2f3d88;
    --photo-sky: #7f8586;
    --photo-brick: #3b2a20;
    --photo-dark: #1c1713;
    --photo-orange: #a8661e;
  }
  * { margin: 0; padding: 0; box-sizing: border-box; }
  html, body {
    width: 1200px;
    height: 1200px;
    overflow: hidden;
    background: var(--page-bg);
  }
  .billboard {
    position: absolute;
    left: 150px;
    top: 80px;
    width: 900px;
    height: 1040px;
    overflow: hidden;
    background: var(--photo-dark);
  }
  .site-photo {
    position: absolute;
    inset: 0;
    background:
      radial-gradient(ellipse 45% 40% at 72% 62%, rgba(168,102,30,0.75), rgba(168,102,30,0) 70%),
      linear-gradient(180deg, var(--photo-sky) 0%, #5c5a56 12%, var(--photo-brick) 24%, #2e221b 60%, var(--photo-dark) 100%);
  }
  .brand-name {
    position: absolute;
    top: 92px;
    left: 0;
    width: 100%;
    text-align: center;
    font-family: 'Oswald', sans-serif;
    font-weight: 300;
    font-size: 64px;
    letter-spacing: 6px;
    color: var(--white);
  }
  .slogan {
    position: absolute;
    left: 0;
    width: 100%;
    text-align: center;
    font-family: 'Anton', sans-serif;
    color: var(--white);
    line-height: 1;
    text-transform: uppercase;
  }
  .slogan-line-1 { top: 280px; font-size: 118px; }
  .slogan-line-2 { top: 430px; font-size: 112px; }
  .services {
    position: absolute;
    top: 625px;
    left: 0;
    width: 100%;
    display: flex;
    justify-content: center;
    gap: 26px;
    list-style: none;
    font-family: 'Oswald', sans-serif;
    font-weight: 400;
    font-size: 54px;
    line-height: 1;
    color: var(--white);
    text-transform: uppercase;
  }
  .services li::before {
    content: "";
    display: inline-block;
    width: 18px;
    height: 18px;
    border-radius: 50%;
    background: var(--white);
    margin-right: 12px;
    vertical-align: middle;
    position: relative;
    top: -6px;
  }
  .footer-band {
    position: absolute;
    left: 0;
    top: 0;
    width: 900px;
    height: 1040px;
  }
  .contact {
    position: absolute;
    top: 912px;
    left: 0;
    width: 100%;
    display: flex;
    justify-content: center;
    align-items: center;
    gap: 26px;
    color: var(--white);
    font-family: 'Oswald', sans-serif;
  }
  .contact-item { display: flex; align-items: center; gap: 14px; }
  .contact-web { font-weight: 400; font-size: 34px; }
  .contact-phone { font-weight: 600; font-size: 60px; }
  .contact svg { flex: none; }
</style>
</head>
<body>
  <main class="billboard">
    <div class="site-photo" role="img" aria-label="Orange excavator demolishing an old brick building under a grey sky"></div>

    <div class="brand-name">HOLLICK</div>

    <h1 class="slogan slogan-line-1">&ldquo;Call Hollick,</h1>
    <div class="slogan slogan-line-2">Watch It Fall&rdquo;</div>

    <ul class="services">
      <li>Interior</li>
      <li>Exterior</li>
      <li>Commercial</li>
    </ul>

    <svg class="footer-band" viewBox="0 0 900 1040" aria-hidden="true">
      <defs>
        <linearGradient id="bandBlue" x1="0" y1="0" x2="0" y2="1">
          <stop offset="0" stop-color="var(--blue-top)"/>
          <stop offset="0.55" stop-color="var(--blue-mid)"/>
          <stop offset="1" stop-color="var(--blue-bottom)"/>
        </linearGradient>
      </defs>
      <polygon points="0,880 175,732 900,898 900,1040 0,1040" fill="var(--yellow)"/>
      <polygon points="0,904 178,756 900,920 900,1040 0,1040" fill="url(#bandBlue)"/>
    </svg>

    <div class="contact">
      <div class="contact-item contact-web">
        <svg width="54" height="54" viewBox="0 0 54 54" fill="none" stroke="#fff" stroke-width="3">
          <circle cx="27" cy="27" r="24"/>
          <ellipse cx="27" cy="27" rx="11" ry="24"/>
          <line x1="27" y1="3" x2="27" y2="51"/>
          <line x1="3" y1="27" x2="51" y2="27"/>
          <path d="M7 15 H47 M7 39 H47"/>
        </svg>
        <span>www.hollickdemolition.com</span>
      </div>
      <div class="contact-item contact-phone">
        <svg width="58" height="58" viewBox="0 0 58 58" fill="none" stroke="#fff" stroke-width="3" stroke-linejoin="round">
          <path d="M14 6 L22 16 L17 23 C20 31 27 38 35 41 L42 36 L52 44 L46 52 C26 52 6 32 6 12 Z"/>
          <path d="M33 6 A19 19 0 0 1 52 25"/>
          <path d="M32 14 A11 11 0 0 1 44 26"/>
        </svg>
        <span>412-555-0187</span>
      </div>
    </div>
  </main>
</body>
</html>
```